Book title: Lanternfall: The spark of momentum!

This book is called: Lanternfall: The spark of momentum!

A guide to understanding the most popular types of coaching and how to find the perfect coach for you.
The coaching industry has exploded over the past few years as the demand for them has increased. With so many different types of coaches it can be intimidating and overwhelming to find the perfect one for you. To further complicate matters, you may experience times in your life when you require multiple coaches. {Book Title} aims to quite the noise and assist you in finding the perfect coach for you. In this book, you will learn more about the different types of coaching as well as meet a hand-picked selection of coaches from the most popular coaching niches. Each featured coach has provided an exercise designed to move you powerfully forward. We encourage you to work through each exercise so you may experience firsthand the power of working with these incredible coaches.

We would like a professional and simple design. See examples included. We would like to see blood orange included in the design, please see color pallets included as well.

Target Market(s)

Corporate professionals wanting to explore the various types of coaching industry

Industry/Entity Type

Coaching - Health, business, spiritual

Font styles to use
Serif

Colors
EE7325
F08F49
F5BC92
FAE3D3
FDF4ED

Requirements
Must have
• Please include book title: Lanternfall, Subtitle: The spark of momentum! Name of publishing company: Silver Meadow Publishing, Spaces for 8 author names on the front of the cover- Author Name
Nice to have
• A feminine yet corporate feel.
Should not have
• We don't want it

```html
<!DOCTYPE html>
<html lang="en">
<head>
<meta charset="utf-8">
<title>Lanternfall: The spark of momentum! – Book Cover</title>
<link rel="stylesheet" href="https://fonts.googleapis.com/css2?family=Jost:ital,wght@0,400;1,300&family=Spectral:ital,wght@0,400;1,400&display=swap">
<style>
  :root {
    --stage: #bcc4c7;
    --paper: #fdf5ef;
    --magenta: #d6398a;
    --coral: #ee7366;
    --plum: #a22c77;
    --band: #eddcea;
    --sky: #97d8f1;
    --vine: #7f80c4;
    --petal: #efbdd6;
    --ink: #1f1a1d;
  }
  * { margin: 0; padding: 0; box-sizing: border-box; }
  html, body { width: 1200px; height: 900px; overflow: hidden; }
  body { background: var(--stage); position: relative; font-family: "Spectral", Georgia, serif; }

  .cover-panel { position: absolute; top: 126px; height: 648px; background: var(--paper); }
  .front { left: 66px; width: 432px; }
  .spine { left: 565px; width: 72px; }
  .back { left: 702px; width: 432px; }

  .title {
    position: absolute; left: 0; right: 0; top: 62px; text-align: center;
    font-family: "Jost", Arial, sans-serif; font-weight: 400; font-size: 34px;
    letter-spacing: 1.5px; color: var(--magenta); text-transform: uppercase;
  }
  .subtitle {
    position: absolute; left: 0; right: 0; top: 105px; text-align: center;
    font-family: "Jost", Arial, sans-serif; font-weight: 300; font-style: italic;
    font-size: 17px; letter-spacing: 0.5px; color: var(--coral); text-transform: uppercase;
  }
  .ornament-area { position: absolute; border-radius: 12px;
    background: linear-gradient(90deg, rgba(127,128,196,0.15), rgba(239,189,214,0.75), rgba(127,128,196,0.15)); }
  .front .ornament-area { left: 132px; top: 160px; width: 167px; height: 22px; }
  .back .ornament-area { left: 102px; top: 88px; width: 228px; height: 33px; }

  .brain-illustration { position: absolute; left: 132px; top: 218px; width: 167px; height: 215px;
    border-radius: 48% 48% 42% 42% / 40% 40% 55% 55%; background: var(--sky); border: 2px solid #fff; }

  .author-band { position: absolute; left: 0; right: 0; top: 482px; height: 91px; background: var(--band);
    display: flex; flex-direction: column; justify-content: center; align-items: center; }
  .author-line { font-style: italic; font-size: 14px; line-height: 15.5px; color: var(--plum); }

  .publisher { position: absolute; left: 0; right: 0; text-align: center;
    font-family: "Spectral", Georgia, serif; font-weight: 400; color: var(--ink); }
  .front .publisher { top: 597px; font-size: 9px; line-height: 12px; }
  .back .publisher { top: 558px; font-size: 12px; line-height: 16px; }

  .spine-title, .spine-subtitle {
    position: absolute; left: 50%; white-space: nowrap;
    font-family: "Jost", Arial, sans-serif; text-transform: uppercase;
    transform: translate(-50%, -50%) rotate(-90deg);
  }
  .spine-title { top: 473px; font-weight: 400; font-size: 30px; letter-spacing: 1.5px; color: var(--magenta); }
  .spine-subtitle { top: 161px; font-weight: 300; font-style: italic; font-size: 15px; letter-spacing: 0.5px; color: var(--coral); }
  .spine-flower { position: absolute; left: 18px; top: 286px; width: 36px; height: 36px; border-radius: 50%;
    background: radial-gradient(circle, #c98fb3 0 12%, var(--petal) 14% 100%); }

  .blurb { position: absolute; left: 80px; width: 272px; top: 191px; text-align: center;
    font-style: italic; font-size: 10.3px; line-height: 14px; color: var(--plum); }
</style>
</head>
<body>
  <section class="cover-panel front">
    <h1 class="title">Lanternfall</h1>
    <p class="subtitle">The spark of momentum!</p>
    <div class="ornament-area" role="img" aria-label="Decorative vine flourish with a pink flower"></div>
    <div class="brain-illustration" role="img" aria-label="Illustration of a blue brain with white branching vines"></div>
    <div class="author-band">
      <p class="author-line">Marisol Whitaker / Gavin Holloway</p>
      <p class="author-line">Owen Pritchard / Callum Ashbury</p>
      <p class="author-line">Renata Fairlie / Desmond Kearny</p>
      <p class="author-line">Hazel Lindqvist / Priya Castellan</p>
    </div>
    <p class="publisher">Silver Meadow<br>Publishing</p>
  </section>

  <section class="cover-panel spine">
    <p class="spine-subtitle">The spark of momentum!</p>
    <div class="spine-flower" role="img" aria-label="Pink flower ornament"></div>
    <p class="spine-title">Lanternfall</p>
  </section>

  <section class="cover-panel back">
    <div class="ornament-area" role="img" aria-label="Decorative vine flourish with a pink flower"></div>
    <p class="blurb">Lorem ipsum dolor sit amet, consectetuer adipiscing elit, sed diam nonummy nibh euismod tincidunt ut laoreet dolore magna aliquam erat volutpat. Ut wisi enim ad minim veniam, quis nostrud exerci tation ullamcorper suscipit lobortis nisl ut aliquip ex ea commodo consequat. Duis autem vel eum iriure dolor in hendrerit in vulputate velit esse molestie consequat, vel illum dolore eu feugiat nulla facilisis at vero eros et accumsan et iusto odio dignissim qui blandit praesent luptatum zzril delenit augue duis dolore te feugait nulla facilisi.<br>Lorem ipsum dolor sit amet, cons ectetuer adipiscing elit, sed diam nonummy nibh euismod tincidunt ut laoreet dolore magna aliquam erat volutpat. Ut wisi enim ad minim veniam, quis nostrud exerci tation ullamcorper lobortis nisl ut aliquip ex ea commodo consequat. Duis autem vel eum iriure dolor in hendrerit in vulputate velit esse molestie consequat, vel illum dolore eu feugiat nulla facilisis at vero eros et accumsan et iusto odio dignissim qui blandit praesent luptatum zzril delenit augue duis dolore te feugait nulla facilisi.et accumsan et iusto odio dignissim qui blandit praesent luptatum zzril delenit augue duis dolore te feugait nulla facilisi.</p>
    <p class="publisher">Silver Meadow<br>Publishing</p>
  </section>
</body>
</html>
```